pharmacy/travel clinic business card design

We need a business card for our new business called Brenwick Travel Clinic and Pharmacy. Our primary focus is doing consultations for people before travelling internationally and providing vaccinations and prescriptions for them. While the business is considered a pharmacy, it has more the look and feel of a doctor's office. The design should communicate a professional and trustworthy feel. I have attached a copy of the logo we are going to be using.
Updates
Thanks for the submissions.  If you haven`t been eliminated you are one of the finalists.  Decision will likely be made tomorrow.

Target Market(s)
Customers, other health care professionals, travel agents
Industry/Entity Type
Clinic
Look and feel
Each slider illustrates characteristics of the customer's brand and the style your logo design should communicate.

```html
<!DOCTYPE html>
<html lang="en">
<head>
<meta charset="utf-8">
<title>Brenwick Travel Clinic and Pharmacy – Business Card</title>
<link href="https://fonts.googleapis.com/css2?family=Arimo:wght@400;700&display=swap" rel="stylesheet">
<style>
  :root {
    --backdrop: #4a4d4a;
    --card: #ffffff;
    --card-shade: #eef0f0;
    --green: #7cb83a;
    --blue: #2d4b9b;
    --sky: #3d9fd8;
  }
  * { box-sizing: border-box; margin: 0; padding: 0; }
  html, body { width: 1200px; height: 871px; overflow: hidden; }
  body {
    background: var(--backdrop);
    font-family: "Arimo", Arial, sans-serif;
    display: flex;
    flex-direction: column;
    align-items: center;
    justify-content: center;
    gap: 44px;
  }
  .card {
    position: relative;
    width: 630px;
    height: 360px;
    background: linear-gradient(135deg, var(--card) 45%, var(--card-shade) 100%);
    box-shadow: 0 12px 30px rgba(0,0,0,.35);
    overflow: hidden;
  }
  .brand {
    display: flex;
    align-items: center;
    gap: 12px;
  }
  .brand-dot {
    width: 22px; height: 22px;
    border-radius: 50%;
    background: var(--sky);
    flex: none;
  }
  .brand-name {
    color: var(--green);
    font-weight: 700;
    line-height: 1.02;
  }
  /* back side */
  .card-back { display: flex; align-items: center; justify-content: center; }
  .card-back .brand-dot { width: 34px; height: 34px; }
  .card-back .brand-name { font-size: 46px; }
  /* front side */
  .card-front .brand { position: absolute; left: 46px; top: 36px; }
  .card-front .brand-name { font-size: 31px; }
  .holder {
    position: absolute;
    right: 46px; top: 168px;
    text-align: right;
  }
  .holder-name { color: var(--green); font-size: 30px; font-weight: 400; }
  .holder-role { color: var(--blue); font-size: 19px; margin-top: 2px; }
  .contact {
    position: absolute;
    left: 46px; bottom: 40px;
    list-style: none;
    font-size: 19px;
    line-height: 1.75;
    color: var(--blue);
  }
  .contact-label { color: var(--green); font-weight: 700; display: inline-block; width: 30px; }
</style>
</head>
<body>
  <section class="card card-back">
    <div class="brand">
      <span class="brand-dot"></span>
      <span class="brand-name">Brenwick Travel Clinic<br>and Pharmacy</span>
    </div>
  </section>

  <section class="card card-front">
    <div class="brand">
      <span class="brand-dot"></span>
      <span class="brand-name">Brenwick Travel Clinic<br>and Pharmacy</span>
    </div>
    <div class="holder">
      <div class="holder-name">Martin Ellery</div>
      <div class="holder-role">inventor</div>
    </div>
    <ul class="contact">
      <li><span class="contact-label">M:</span>PO Box 456 Ashgrove, Victoria</li>
      <li><span class="contact-label">P:</span>03 9876 5432</li>
      <li><span class="contact-label">W:</span>www.brenwickclinic.com</li>
      <li><span class="contact-label">E:</span>martin.ellery@brenwickclinic.com</li>
    </ul>
  </section>
</body>
</html>
```